Corvella Foundation is a new grant making charity set up in the UK.

Having got a logo, we now need a website to go with it. We have worked out the text which people are going to need in order to then apply for grants. But having found out what we require they will probably need to go away and think about it.
We have to be careful of what images we use. So I have uploaded some images that we like. We are also going to be adding more pages almost immediately so need to think about the images for these.
I know basic wordpress so I will be able to add new pages/make alterations in future.
Updates
The website does need to be coded in Wordpress so that I can maintain it afterwards.
Marisse
Brief changed to provide more money and we have also provided more possible pictures. And generally more explanation.
Target Market(s)
departments in universities, other charities doing work on relief of pain, people working in health service departments
Industry/Entity Type
Health Charity
Coding
Coded - Design and coding required
Number of Pages Required
4 page
Look and feel
Each slider illustrates characteristics of the customer's brand and the style your logo design should communicate.

```html
<!DOCTYPE html>
<html lang="en">
<head>
<meta charset="utf-8">
<title>Corvella Foundation</title>
<link href="https://fonts.googleapis.com/css2?family=Playfair+Display:wght@700&family=Source+Sans+3:wght@400;600;700&display=swap" rel="stylesheet">
<style>
:root{
  --blue:#0565bf;
  --blue-btn:#1a86d4;
  --ink:#111820;
  --text:#2a2f36;
  --muted:#6b7380;
  --navy:#0b2436;
  --line:#cfd6de;
  --card:#f7f8fa;
  --white:#ffffff;
}
*{box-sizing:border-box;margin:0;padding:0}
html,body{width:1200px;height:4123px;overflow:hidden}
body{position:relative;font-family:"Source Sans 3",Arial,sans-serif;color:var(--text);background:var(--white)}
.abs{position:absolute}
.serif{font-family:"Playfair Display",Georgia,serif;font-weight:700;color:var(--ink);letter-spacing:.5px}
.brand{font-weight:700;color:var(--blue);font-size:20px;letter-spacing:.5px;display:flex;align-items:center;gap:8px}
.brand-mark{width:14px;height:14px;background:var(--blue)}
.btn{position:absolute;display:flex;align-items:center;justify-content:center;gap:12px;background:var(--blue-btn);color:var(--white);font-weight:600;font-size:15px;border-radius:26px}
.btn svg{width:16px;height:10px}

/* header */
.site-header{top:0;left:0;width:1200px;height:80px;background:var(--white)}
.site-header .brand{position:absolute;left:70px;top:26px}
.nav{position:absolute;left:658px;top:31px;display:flex;gap:22px;font-size:13px;font-weight:600;color:var(--ink)}
.nav span.dot{color:var(--ink)}
.nav .active{color:var(--blue)}
.reg{position:absolute;left:1003px;top:22px;font-size:12px;color:var(--text)}
.reg b{display:block;color:var(--blue);font-size:16px;font-weight:700;margin-top:2px}

/* hero */
.hero{top:80px;left:0;width:1200px;height:555px;background:radial-gradient(circle at 70% 45%,#e9ecef,#cfd3d8 70%,#c4c8cd)}
.hero .kicker{left:70px;top:134px;color:var(--blue);font-size:15px;font-weight:600}
.hero h1{left:70px;top:160px;font-size:54px;line-height:61px}
.hero .btn{left:70px;top:370px;width:164px;height:50px}
.dots{left:70px;top:483px;display:flex;gap:10px}
.dots i{display:block;width:32px;height:4px;background:#8c8f94}
.dots i:first-child{background:var(--blue)}

/* welcome */
.welcome-art{left:85px;top:683px}
.welcome .kicker{left:626px;top:843px;color:var(--blue);font-size:20px;font-weight:600}
.welcome h2{left:626px;top:866px;font-size:54px;line-height:52px}
.welcome p{left:626px;top:985px;width:500px;font-size:14px;line-height:23px}

/* about */
.about{top:1267px;left:0;width:1200px;height:565px;background:var(--blue)}
.about h2{left:70px;top:63px;font-size:54px;color:var(--white)}
.faq{left:70px;width:519px;border:1px solid rgba(255,255,255,.7);color:var(--white);font-size:14px;font-weight:600;padding:0 15px}
.faq .q{height:40px;display:flex;align-items:center;justify-content:space-between}
.faq .a{font-weight:400;line-height:22px;padding-bottom:14px}
.faq svg{width:22px;height:22px}
.about-art{left:627px;top:39px}

/* grants */
.grants-art{left:85px;top:1868px}
.grants h2{left:613px;top:1985px;font-size:54px}
.grants p{left:613px;top:2057px;width:500px;font-size:14px;line-height:22px}
.grants .btn{left:613px;top:2173px;width:162px;height:51px}

/* education */
.edu{top:2448px;left:0;width:1200px;height:565px;background:var(--blue);color:var(--white)}
.edu .sub{left:0;width:1200px;top:86px;text-align:center;font-size:17px;font-weight:600}
.edu h2{left:0;width:1200px;top:108px;text-align:center;color:var(--white);font-size:54px}
.topic{display:flex;align-items:center;gap:18px;font-size:17px;font-weight:600;line-height:24px}
.topic .ic{position:relative;width:114px;height:114px}
.topic .ic::after{content:"";position:absolute;right:-4px;bottom:-4px;width:60px;height:60px;border-right:2px solid #fff;border-bottom:2px solid #fff}
.topic .ic svg{width:114px;height:114px}

/* contact */
.contact-art{left:70px;top:3100px}
.contact h2{left:610px;top:3108px;font-size:44px}
.field{position:absolute;border:1px solid #8d949c;border-radius:30px;font-size:14px;color:var(--text);padding:16px 16px}
.field.msg{border-radius:12px}
.contact .btn{left:613px;top:3506px;width:162px;height:50px}

/* footer */
.foot-band{left:0;top:3744px;width:1200px;height:379px;background:var(--navy)}
.foot-card{left:70px;top:3672px;width:1060px;height:365px;background:var(--card)}
.foot-brand{left:90px;top:3712px;width:224px;height:100px;background:var(--white)}
.foot-brand .brand{position:absolute;left:17px;top:86px}
.foot-about{left:107px;top:3854px;width:250px;font-size:13px;line-height:21px}
.fcol h4{display:flex;align-items:center;gap:10px;color:var(--blue);font-size:13px;font-weight:700;letter-spacing:.5px}
.fcol h4::before{content:"";width:24px;height:2px;background:var(--blue)}
.fcol ul{list-style:none;margin-top:20px;font-size:13px;line-height:36px}
.fcol p{font-size:13px;line-height:21px;margin-top:20px}
.nl-input{left:861px;top:3882px;width:237px;height:38px;border:1px solid #b8c0c8;border-radius:20px;font-size:12px;color:var(--muted);display:flex;align-items:center;gap:8px;padding-left:12px}
.nl-btn{left:861px;top:3930px;width:237px;height:38px;border-radius:20px;background:var(--blue);color:#fff;font-size:13px;font-weight:700;display:flex;align-items:center;justify-content:center}
.to-top{left:575px;top:4012px;width:50px;height:50px;border-radius:50%;background:var(--blue-btn);display:flex;align-items:center;justify-content:center}
.copy{left:0;top:4074px;width:1200px;text-align:center;font-size:12px;color:#8d99a6}
.copy span{color:var(--blue-btn)}
</style>
</head>
<body>

<header class="abs site-header">
  <div class="brand"><span class="brand-mark"></span>CORVELLA FOUNDATION</div>
  <nav class="nav"><span class="active">Home</span><span class="dot">•</span><span>About</span><span class="dot">•</span><span>Grants</span><span class="dot">•</span><span>Contact</span></nav>
  <div class="reg">Charity Registration NO.<b>1048876</b></div>
</header>

<section class="abs hero" role="img" aria-label="Soft grey background of faint nerve cells">
  <div class="abs kicker">Corvella Foundation is a grant</div>
  <h1 class="abs serif">Making Charity<br>Set up in the<br>UK in 2021</h1>
  <a class="btn">Know More <svg viewBox="0 0 16 10"><path d="M0 5h13M9 1l4 4-4 4" stroke="#fff" stroke-width="2" fill="none"/></svg></a>
  <div class="abs dots"><i></i><i></i><i></i></div>
</section>

<section class="welcome">
  <svg class="abs welcome-art" width="515" height="512" viewBox="0 0 515 512">
    <defs><linearGradient id="crowd" x1="0" y1="0" x2="1" y2="1"><stop offset="0" stop-color="#f08a2c"/><stop offset=".35" stop-color="#e94f8a"/><stop offset=".65" stop-color="#8fc84a"/><stop offset="1" stop-color="#f3d630"/></linearGradient></defs>
    <path d="M12 510V230A243 220 0 0 1 498 230V510" fill="none" stroke="var(--blue)" stroke-width="3"/>
    <path d="M0 512V240A245 230 0 0 1 490 240V512Z" fill="url(#crowd)" role="img" aria-label="Colourful silhouettes of a crowd of people"/>
  </svg>
  <div class="abs kicker">Welcome to</div>
  <h2 class="abs serif">Corvella<br>Foundation</h2>
  <p class="abs">Corvella Foundation is a grant making charity set up in the UK in 2021 The main aim of Corvella Foundation is to reduce the suffering caused by chronic pain.Charity registration number 1048876.</p>
</section>

<section class="abs about">
  <h2 class="abs serif">About Us</h2>
  <div class="abs faq" style="top:135px">
    <div class="q">Q. Who are the trustees of Corvella Foundation?<svg viewBox="0 0 22 22"><circle cx="11" cy="11" r="9.5" fill="none" stroke="#fff" stroke-width="1.5"/><path d="M7 9l4 4 4-4" fill="none" stroke="#fff" stroke-width="1.5"/></svg></div>
    <div class="a">A. The initial trustees are Marisse, Peter &amp; Adrian Holloway.<br>A fourth trustee is about to be appointed, the legal firm of Ashcombe Legal.</div>
  </div>
  <div class="abs faq" style="top:261px"><div class="q">Q. Who are the medical advisers to Corvella Foundation?<svg viewBox="0 0 22 22"><circle cx="11" cy="11" r="9.5" fill="none" stroke="#fff" stroke-width="1.5"/><path d="M9 7l4 4-4 4" fill="none" stroke="#fff" stroke-width="1.5"/></svg></div></div>
  <div class="abs faq" style="top:311px"><div class="q">Q. How much money does Corvella Foundation have?<svg viewBox="0 0 22 22"><circle cx="11" cy="11" r="9.5" fill="none" stroke="#fff" stroke-width="1.5"/><path d="M9 7l4 4-4 4" fill="none" stroke="#fff" stroke-width="1.5"/></svg></div></div>
  <div class="abs faq" style="top:361px"><div class="q">Q. Where has this money come from?<svg viewBox="0 0 22 22"><circle cx="11" cy="11" r="9.5" fill="none" stroke="#fff" stroke-width="1.5"/><path d="M9 7l4 4-4 4" fill="none" stroke="#fff" stroke-width="1.5"/></svg></div></div>
  <div class="abs faq" style="top:411px"><div class="q">Q. Why is the foundation named after Marisse Holloway?<svg viewBox="0 0 22 22"><circle cx="11" cy="11" r="9.5" fill="none" stroke="#fff" stroke-width="1.5"/><path d="M9 7l4 4-4 4" fill="none" stroke="#fff" stroke-width="1.5"/></svg></div></div>
  <svg class="abs about-art" width="501" height="498" viewBox="0 0 501 498">
    <defs><linearGradient id="words" x1="0" y1="0" x2="1" y2="1"><stop offset="0" stop-color="#3a2a3c"/><stop offset=".5" stop-color="#241a2e"/><stop offset="1" stop-color="#5b4a30"/></linearGradient></defs>
    <path d="M0 0H501V250A250 248 0 0 1 0 250Z" fill="url(#words)" role="img" aria-label="Word cloud about cannabis, pain and public health"/>
    <path d="M0 0H155V125A30 30 0 0 1 125 155H0Z" fill="#fff"/>
  </svg>
</section>

<section class="grants">
  <svg class="abs grants-art" width="510" height="500" viewBox="0 0 510 500">
    <defs><radialGradient id="neuron" cx=".45" cy=".45" r=".6"><stop offset="0" stop-color="#f2e6f5"/><stop offset=".35" stop-color="#7a80c8"/><stop offset="1" stop-color="#1b2a5c"/></radialGradient></defs>
    <path d="M490 140A250 250 0 0 1 160 488" fill="none" stroke="var(--blue)" stroke-width="3"/>
    <circle cx="246" cy="246" r="240" fill="url(#neuron)" role="img" aria-label="Glowing nerve cells under a microscope"/>
  </svg>
  <h2 class="abs serif">Grants</h2>
  <p class="abs">Grants will almost entirely be provided for research or education into pain management, or the prevention of pain.The trustees will also be providing grants to a number of other charities or to areas with which they have had a long term association, such as HIV/AIDS and TB.</p>
  <a class="btn">Read More <svg viewBox="0 0 16 10"><path d="M0 5h13M9 1l4 4-4 4" stroke="#fff" stroke-width="2" fill="none"/></svg></a>
</section>

<section class="abs edu">
  <div class="abs sub">The main categories of funding for pain research or</div>
  <h2 class="abs serif">Education will be as Follows</h2>

  <div class="abs topic" style="left:112px;top:203px"><div class="ic"><svg viewBox="0 0 114 114"><circle cx="57" cy="57" r="57" fill="#fff"/><path d="M57 80C34 64 30 54 34 45c4-9 17-10 23-1 6-9 19-8 23 1 4 9 0 19-23 35Z" fill="none" stroke="var(--blue)" stroke-width="2.5"/><path d="M44 52l8 6-4 6 10 4" fill="none" stroke="var(--blue)" stroke-width="2"/></svg></div>Pain Centres</div>
  <div class="abs topic" style="left:445px;top:203px"><div class="ic"><svg viewBox="0 0 114 114"><circle cx="57" cy="57" r="57" fill="#fff"/><rect x="43" y="32" width="28" height="10" rx="2" fill="none" stroke="var(--blue)" stroke-width="2.5"/><rect x="40" y="42" width="34" height="44" rx="5" fill="none" stroke="var(--blue)" stroke-width="2.5"/><path d="M40 56h34M40 72h34" stroke="var(--blue)" stroke-width="2"/></svg></div>The use of opioids</div>
  <div class="abs topic" style="left:821px;top:203px"><div class="ic"><svg viewBox="0 0 114 114"><circle cx="57" cy="57" r="57" fill="#fff"/><path d="M30 70h12l14 6h14l12-8c4-2 6 2 3 5L70 86H44l-14-4" fill="none" stroke="var(--blue)" stroke-width="2.5"/><circle cx="54" cy="42" r="8" fill="none" stroke="var(--blue)" stroke-width="2.5"/><rect x="66" y="36" width="18" height="10" rx="5" fill="none" stroke="var(--blue)" stroke-width="2.5"/></svg></div>Improving the<br>use of medication</div>

  <div class="abs topic" style="left:112px;top:355px"><div class="ic"><svg viewBox="0 0 114 114"><circle cx="57" cy="57" r="57" fill="#fff"/><path d="M28 48l29-12 29 12-29 12Z" fill="none" stroke="var(--blue)" stroke-width="2.5"/><path d="M40 54v14c10 7 24 7 34 0V54M86 48v16" fill="none" stroke="var(--blue)" stroke-width="2.5"/><circle cx="40" cy="80" r="4" fill="none" stroke="var(--blue)" stroke-width="2"/></svg></div>Education</div>
  <div class="abs topic" style="left:445px;top:355px"><div class="ic"><svg viewBox="0 0 114 114"><circle cx="57" cy="57" r="57" fill="#fff"/><rect x="28" y="46" width="58" height="22" rx="11" transform="rotate(-45 57 57)" fill="none" stroke="var(--blue)" stroke-width="2.5"/><rect x="48" y="48" width="18" height="18" transform="rotate(-45 57 57)" fill="none" stroke="var(--blue)" stroke-width="2"/></svg></div>Improved types<br>of pain control</div>
  <div class="abs topic" style="left:821px;top:355px"><div class="ic"><svg viewBox="0 0 114 114"><circle cx="57" cy="57" r="57" fill="#fff"/><path d="M48 86V74c-8-4-12-12-11-21 1-12 11-20 22-19 12 1 20 10 19 21l6 10h-6v7c0 3-2 5-5 5h-7v9" fill="none" stroke="var(--blue)" stroke-width="2.5"/><path d="M56 46l-4 8h8l-4 8" fill="none" stroke="var(--blue)" stroke-width="2"/></svg></div>Measuring pain</div>
</section>

<section class="contact">
  <svg class="abs contact-art" width="510" height="510" viewBox="0 0 510 510">
    <defs><radialGradient id="cells" cx=".5" cy=".55" r=".6"><stop offset="0" stop-color="#9cc6f0"/><stop offset=".45" stop-color="#2f6fc0"/><stop offset="1" stop-color="#0c2f6e"/></radialGradient></defs>
    <path d="M506 10V255A251 251 0 0 1 255 506" fill="none" stroke="var(--blue)" stroke-width="3"/>
    <path d="M0 4H500V250A250 250 0 0 1 0 250Z" fill="url(#cells)" role="img" aria-label="Blue network of nerve cells"/>
    <circle cx="76" cy="76" r="76" fill="#fff"/>
  </svg>
  <h2 class="abs serif">Get In Touch</h2>
  <div class="field" style="left:610px;top:3186px;width:256px;height:56px">First Name</div>
  <div class="field" style="left:872px;top:3186px;width:256px;height:56px">Last name</div>
  <div class="field" style="left:610px;top:3253px;width:256px;height:56px">Email</div>
  <div class="field" style="left:872px;top:3253px;width:256px;height:56px">Phone</div>
  <div class="field msg" style="left:610px;top:3322px;width:518px;height:166px">Your Message</div>
  <a class="btn">Send Now <svg viewBox="0 0 16 10"><path d="M0 5h13M9 1l4 4-4 4" stroke="#fff" stroke-width="2" fill="none"/></svg></a>
</section>

<footer>
  <div class="abs foot-band"></div>
  <div class="abs foot-card"></div>
  <div class="abs foot-brand"></div>
  <div class="abs brand" style="left:107px;top:3808px"><span class="brand-mark"></span>CORVELLA FOUNDATION</div>
  <p class="abs foot-about">Corvella Foundation is a grant making charity set up in the UK in 2021.The main aim of Corvella Foundation is to reduce the suffering caused by chronic pain.</p>
  <div class="abs fcol" style="left:424px;top:3795px"><h4>QUICK LINKS</h4><ul><li>Home</li><li>About</li><li>Grants</li><li>Contact</li></ul></div>
  <div class="abs fcol" style="left:606px;top:3795px"><h4>CONTACT US</h4><p>12 Harbour Lane, Kestrel Bay<br>Northshire, United Kingdom</p><p style="margin-top:14px">info@corvellafoundation.org</p><p style="margin-top:14px">01 234 567 890</p></div>
  <div class="abs fcol" style="left:861px;top:3795px"><h4>NEWSLETTER</h4><p style="margin-top:14px">Subscribe to our newsletter to<br>get more informations</p></div>
  <div class="abs nl-input"><svg width="14" height="10" viewBox="0 0 14 10"><rect x=".5" y=".5" width="13" height="9" fill="none" stroke="#8d949c"/><path d="M.5.5l6.5 5 6.5-5" fill="none" stroke="#8d949c"/></svg>Enter your email address</div>
  <div class="abs nl-btn">Subscribe</div>
  <div class="abs to-top"><svg width="16" height="18" viewBox="0 0 16 18"><path d="M8 17V2M2 8l6-6 6 6" fill="none" stroke="#fff" stroke-width="2"/></svg></div>
  <div class="abs copy">© 2021 <span>Corvella Foundation</span>. All right reserved</div>
</footer>

</body>
</html>
```